MAREK DOLVANE FOR CONGRESS DISTRICT 32

I need to create a campaign flyer for my congress campaign. I am running for congress in District 32 of Texas as a republican. I am a former Olympic athlete, world champion fencer, Army veteran, Counterintelligence officer (I catch spies).
I want just my first name MAREK in big letters at the top. I want it to say MAREK and below it Republican for Congress.
www.marekforcongress.example

Industry/Entity Type

Political

Colors
EB3D1F
EC4F4E
F09395
F8D3D4
FCEDEE

Requirements
Nice to have
• Would love a catchy title for the Flyer like "Spy Catcher", "Olympic Athlete" "World Champion Fencer" running for Congress in your District!

```html
<!DOCTYPE html>
<html lang="en">
<head>
<meta charset="utf-8">
<title>Marek Dolvane for Congress District 32</title>
<link rel="stylesheet" href="https://fonts.googleapis.com/css2?family=Oswald:wght@700&family=Lexend:wght@500;600;700;800&display=swap">
<style>
  :root {
    --navy: #1e2b5e;
    --red: #d11f26;
    --gold: #ffcb05;
    --sky: #8c9fd1;
    --mist: #e4e4e8;
    --white: #ffffff;
    --ink: #1b1d2a;
    --stage: #ecebe8;
  }
  html, body {
    margin: 0;
    width: 1200px;
    height: 1117px;
    overflow: hidden;
    background: var(--stage);
  }
  .flyer {
    position: absolute;
    left: 232px;
    top: 38px;
    width: 735px;
    height: 1040px;
    background: var(--white);
    box-shadow: 0 6px 24px rgba(0,0,0,.12);
  }
  .flyer svg { display: block; }
  .headline { font-family: "Oswald", "Arial Narrow", sans-serif; font-weight: 700; }
  .sans { font-family: "Lexend", "Helvetica Neue", Arial, sans-serif; }
  .fill-navy { fill: var(--navy); }
  .fill-red { fill: var(--red); }
  .fill-gold { fill: var(--gold); }
  .fill-sky { fill: var(--sky); }
  .fill-white { fill: var(--white); }
  .fill-ink { fill: var(--ink); }
</style>
</head>
<body>
<main class="flyer">
  <svg width="735" height="1040" viewBox="0 0 735 1040" xmlns="http://www.w3.org/2000/svg">
    <defs>
      <linearGradient id="portrait-tone" x1="0" y1="0" x2="0" y2="1">
        <stop offset="0" stop-color="#e4e4e8"/>
        <stop offset="1" stop-color="#f1f3f7"/>
      </linearGradient>
      <linearGradient id="corner-sheen" x1="1" y1="0" x2="0" y2="1">
        <stop offset="0" stop-color="#6a78a8"/>
        <stop offset="0.6" stop-color="#1e2b5e"/>
      </linearGradient>
      <linearGradient id="chevron-sheen" x1="0" y1="0" x2="0" y2="1">
        <stop offset="0.7" stop-color="#1e2b5e"/>
        <stop offset="1" stop-color="#3a4880"/>
      </linearGradient>
    </defs>

    <!-- candidate portrait area -->
    <polygon class="candidate-portrait" role="img" aria-label="Portrait photo of the candidate in a light patterned shirt"
             points="649,0 735,0 735,621 493,621 493,362 332,235" fill="url(#portrait-tone)"/>

    <!-- top chevron -->
    <polygon class="fill-sky accent-wedge" points="0,225 87,272 0,334"/>
    <path class="title-chevron" fill="url(#chevron-sheen)" d="M0 0 H649 L236 304 Q205 328 172 311 L0 225 Z"/>

    <text class="headline fill-white" x="60" y="150" font-size="124" textLength="370" lengthAdjust="spacingAndGlyphs">OLYMPIC</text>
    <text class="headline fill-gold" x="58" y="225" font-size="86" textLength="264" lengthAdjust="spacingAndGlyphs">ATHLETE</text>

    <!-- tagline -->
    <g class="sans fill-navy tagline" font-weight="700" font-size="35" text-anchor="middle">
      <text x="235" y="380">RUNNING FOR</text>
      <text x="235" y="417" textLength="376" lengthAdjust="spacingAndGlyphs">CONGRESS IN YOUR</text>
      <text x="235" y="454">DISTRICT!</text>
    </g>

    <!-- vote mark -->
    <text class="sans fill-navy vote-word" x="60" y="609" font-size="156" font-weight="800" textLength="445" lengthAdjust="spacingAndGlyphs">VOTE</text>
    <path class="vote-tick" d="M196 530 L235 582 L310 476" fill="none" stroke="var(--white)" stroke-width="16" stroke-linejoin="round"/>
    <path class="vote-tick" d="M196 530 L235 582 L310 476" fill="none" stroke="var(--red)" stroke-width="9" stroke-linecap="round" stroke-linejoin="round"/>

    <!-- name band -->
    <rect class="fill-red name-band" x="0" y="621" width="735" height="159"/>
    <text class="sans fill-white candidate-name" x="57" y="710" font-size="74" font-weight="800" textLength="620" lengthAdjust="spacingAndGlyphs">MAREK DOLVANE</text>
    <text class="sans fill-white office" x="57" y="757" font-size="42" font-weight="600" textLength="620" lengthAdjust="spacingAndGlyphs">FOR CONGRESS DISTRICT 32</text>

    <!-- platform -->
    <g class="platform sans" font-size="22" font-weight="500">
      <g class="plank">
        <circle class="fill-navy" cx="80" cy="817" r="9"/>
        <path d="M75.5 817 L79 820.5 L85 813.5" fill="none" stroke="var(--white)" stroke-width="2.2" stroke-linecap="round" stroke-linejoin="round"/>
        <text class="fill-ink" x="103" y="825">Stop the devaluation of the dollar.</text>
      </g>
      <g class="plank">
        <circle class="fill-navy" cx="80" cy="857" r="9"/>
        <path d="M75.5 857 L79 860.5 L85 853.5" fill="none" stroke="var(--white)" stroke-width="2.2" stroke-linecap="round" stroke-linejoin="round"/>
        <text class="fill-ink" x="103" y="865" textLength="535" lengthAdjust="spacingAndGlyphs">Secure the border and protect our citizens.</text>
      </g>
      <g class="plank">
        <circle class="fill-navy" cx="80" cy="896" r="9"/>
        <path d="M75.5 896 L79 899.5 L85 892.5" fill="none" stroke="var(--white)" stroke-width="2.2" stroke-linecap="round" stroke-linejoin="round"/>
        <text class="fill-ink" x="103" y="904">Protect constitutional rights.</text>
      </g>
      <g class="plank">
        <circle class="fill-navy" cx="80" cy="936" r="9"/>
        <path d="M75.5 936 L79 939.5 L85 932.5" fill="none" stroke="var(--white)" stroke-width="2.2" stroke-linecap="round" stroke-linejoin="round"/>
        <text class="fill-ink" x="103" y="944">Honor and Support Veterans.</text>
      </g>
    </g>

    <!-- dot grid -->
    <g class="fill-navy dot-grid">
      <circle cx="148" cy="979" r="1.6"/><circle cx="162" cy="979" r="1.6"/><circle cx="176" cy="979" r="1.6"/><circle cx="189" cy="979" r="1.6"/><circle cx="203" cy="979" r="1.6"/><circle cx="217" cy="979" r="1.6"/><circle cx="230" cy="979" r="1.6"/>
      <circle cx="148" cy="993" r="1.6"/><circle cx="162" cy="993" r="1.6"/><circle cx="176" cy="993" r="1.6"/><circle cx="189" cy="993" r="1.6"/><circle cx="203" cy="993" r="1.6"/><circle cx="217" cy="993" r="1.6"/><circle cx="230" cy="993" r="1.6"/>
      <circle cx="148" cy="1007" r="1.6"/><circle cx="162" cy="1007" r="1.6"/><circle cx="176" cy="1007" r="1.6"/><circle cx="189" cy="1007" r="1.6"/><circle cx="203" cy="1007" r="1.6"/><circle cx="217" cy="1007" r="1.6"/><circle cx="230" cy="1007" r="1.6"/>
    </g>

    <!-- corner accents -->
    <polygon class="fill-red corner-left" points="0,943 127,1040 0,1040"/>
    <polygon class="fill-navy corner-right" points="465,1040 735,834 735,1040"/>
    <polygon class="corner-right-sheen" fill="url(#corner-sheen)" points="600,1040 735,872 735,1040" opacity="0.9"/>
  </svg>
</main>
</body>
</html>
```